DrivPeak Agile Coaching Website

I need an updated website for www.drivpeak.example. I'm looking for a modern look. This is a professional site, but I don't want it to look "stuffy". It needs to have an element of fun and learning.

My services include:
Lean Agile Coaching
Lean Agile Training
Facilitation
Workshops
Consulting

Ideas this site should convey: collaboration, learning, teamwork, adaptability, flow, limited WIP, agility, Lean.

I would like to use some of my own photos and slide decks for content: http://www.deckvault.example/mornbeck/presentations

I would also like to include the Peerlinko recommendations I have from customers: https://www.peerlinko.example/in/mornbeck

Examples of sites I like:
http://www.quarrelmosswidget.example
http://www.forthsprintly.example

Target Market(s)

IT professionals, software development managers

Industry/Entity Type

It Company

Coding

Coded - Design and coding required

Font styles to use
Serif
Sans Serif

Requirements
Must have
• Original looking graphics and layout.
• My logo must be included in layout.
• Need to feature my blog content.
• Deliverable must be a WordPress theme that I can install.
• Responsive site.
Nice to have
• Use images from my slides on Deckvault if they make sense.

```html
<!DOCTYPE html>
<html lang="en">
<head>
<meta charset="utf-8">
<title>DrivPeak — Lean Agile Coaching</title>
<link rel="stylesheet" href="https://fonts.googleapis.com/css2?family=Open+Sans:wght@400;600&family=Source+Sans+Pro:wght@600;700&display=swap">
<style>
  :root{
    --green:#00c832;
    --ink:#111111;
    --text:#555555;
    --muted:#6a6a6a;
    --link-red:#c8102e;
    --footer:#4f4f4f;
    --white:#ffffff;
  }
  *{box-sizing:border-box;margin:0;padding:0}
  html,body{width:714px;height:1200px;overflow:hidden;background:var(--white)}
  body{position:relative;font-family:"Open Sans",Arial,sans-serif;color:var(--text)}
  .abs{position:absolute}

  .top-rule{left:0;top:0;width:714px;height:3px;background:var(--green)}
  .site-header{left:0;top:3px;width:714px;height:57px}
  .brand{left:59px;top:16px;display:flex;align-items:center;gap:4px;
    font-family:"Source Sans Pro",Arial,sans-serif;font-weight:700;font-size:22px;color:var(--ink);letter-spacing:-.5px}
  .brand-mark{width:4px;height:18px;background:var(--green)}
  .main-nav{top:26px;font-size:7px;color:var(--ink);letter-spacing:.2px}
  .main-nav.active{color:var(--green)}
  .search-icon{left:631px;top:25px}

  .hero{left:0;top:60px;width:714px;height:313px;
    background:linear-gradient(180deg,#5b4a3e 0%,#8a7b70 30%,#bdb3aa 55%,#2c2a2b 70%,#d9d6d2 100%)}

  .section-title{left:0;width:714px;text-align:center;font-family:"Source Sans Pro",Arial,sans-serif;
    font-weight:700;font-size:21px;color:var(--ink);letter-spacing:.3px}
  .section-title span{color:var(--green)}
  .section-intro{left:130px;width:454px;text-align:center;font-size:7.1px;line-height:12.4px;color:var(--text)}

  .service{width:180px;text-align:center}
  .service-badge{width:82px;height:82px;margin:0 auto;display:block}
  .service-title{margin-top:10px;font-family:"Source Sans Pro",Arial,sans-serif;font-weight:700;font-size:8.8px;color:#333;letter-spacing:.4px}
  .service-text{margin-top:10px;font-size:7.1px;line-height:12.2px;color:var(--text);padding:0 12px}
  .service-more{margin-top:9px;font-size:7px;color:var(--link-red)}

  .post{width:189px}
  .post-frame{border:1px solid #dcdcdc;padding:2px;height:121px}
  .post-image{width:100%;height:100%}
  .post-title{margin-top:14px;font-family:"Source Sans Pro",Arial,sans-serif;font-weight:700;font-size:8.6px;color:#333;letter-spacing:.3px}
  .post-text{margin-top:6px;font-size:7px;line-height:12.6px;color:var(--muted)}
  .post-more{margin-top:7px;font-family:"Source Sans Pro",Arial,sans-serif;font-weight:700;font-size:8px;color:var(--green);letter-spacing:.3px}

  .site-footer{left:0;top:1013px;width:714px;height:147px;background:var(--footer);color:#e8e8e8}
  .footer-col{top:1032px}
  .footer-heading{font-size:11.2px;color:var(--white);margin-bottom:3px}
  .footer-col li{list-style:none;font-size:7.6px;line-height:15.2px;color:#e2e2e2}
  .newsletter-note{font-size:7.6px;color:#e2e2e2;line-height:12px}
  .newsletter-input{margin-top:6px;width:163px;height:20px;background:var(--white);font-size:6.4px;color:#777;padding:6px 8px}
  .newsletter-button{margin-top:6px;width:69px;height:20px;background:var(--green);color:var(--white);
    font-family:Arial,sans-serif;font-weight:700;font-size:8.2px;text-align:center;line-height:20px}

  .legal-bar{left:0;top:1160px;width:714px;height:40px;background:var(--green)}
  .legal-text{left:85px;top:1175px;font-size:6.8px;color:var(--white)}
  .social-links{left:577px;top:1174px;display:flex;gap:4px}
  .social-chip{width:13px;height:13px;border-radius:2px;background:var(--white)}
</style>
</head>
<body>
  <div class="abs top-rule"></div>

  <header class="abs site-header">
    <div class="abs brand"><span class="brand-mark"></span>DrivPeak</div>
    <nav>
      <span class="abs main-nav active" style="left:438px">HOME</span>
      <span class="abs main-nav" style="left:480px">ABOUT</span>
      <span class="abs main-nav" style="left:524px">CONTACT</span>
      <span class="abs main-nav" style="left:577px">SERVICES</span>
    </nav>
  </header>
  <svg class="abs search-icon" width="10" height="10" viewBox="0 0 10 10" aria-label="Search">
    <circle cx="4" cy="4" r="3" fill="none" stroke="#111" stroke-width="1.5"/>
    <line x1="6.2" y1="6.2" x2="9" y2="9" stroke="#111" stroke-width="1.8" stroke-linecap="round"/>
  </svg>

  <div class="abs hero" role="img" aria-label="Photo of a team gathered around a table playing a flow simulation game with cards, dice and charts"></div>

  <h2 class="abs section-title" style="top:402px">OUR <span>SERVICES</span></h2>
  <p class="abs section-intro" style="top:440px">Knowledge work endeavors such as software development projects seem anything but clear when in process. One can demand all the detailed status reports, stakeholder update meetings, and reassurances in the world</p>

  <div class="abs service" style="left:68px;top:499px">
    <svg class="service-badge" viewBox="0 0 82 82" aria-hidden="true">
      <circle cx="41" cy="41" r="40" fill="var(--green)"/>
      <circle cx="41" cy="41" r="35" fill="none" stroke="#fff" stroke-width="2"/>
      <path d="M40 30 L55 42 L52 42 L52 54 L36 54 L36 42 L33 42 Z" fill="#fff"/>
      <circle cx="30" cy="42" r="4" fill="#fff"/>
      <path d="M22 55 Q22 47 30 47 Q38 47 38 55 Z" fill="#fff"/>
    </svg>
    <div class="service-title">LEAN AGILE COACHING</div>
    <p class="service-text">Knowledge work endeavors such as software development projects seem anything but clear when in process. One can demand</p>
    <div class="service-more">READMORE</div>
  </div>

  <div class="abs service" style="left:266px;top:499px">
    <svg class="service-badge" viewBox="0 0 82 82" aria-hidden="true">
      <circle cx="41" cy="41" r="40" fill="var(--green)"/>
      <circle cx="41" cy="41" r="35" fill="none" stroke="#fff" stroke-width="2"/>
      <circle cx="41" cy="36" r="11" fill="none" stroke="#fff" stroke-width="2"/>
      <ellipse cx="41" cy="36" rx="5" ry="11" fill="none" stroke="#fff" stroke-width="1.5"/>
      <line x1="30" y1="36" x2="52" y2="36" stroke="#fff" stroke-width="1.5"/>
      <path d="M24 52 Q34 48 42 52 L54 50 Q58 50 56 54 L44 58 Q34 58 24 56 Z" fill="#fff"/>
    </svg>
    <div class="service-title">FACILITATION</div>
    <p class="service-text">Knowledge work endeavors such as software development projects seem anything but clear when in process. One can demand</p>
    <div class="service-more">READMORE</div>
  </div>

  <div class="abs service" style="left:465px;top:499px">
    <svg class="service-badge" viewBox="0 0 82 82" aria-hidden="true">
      <circle cx="41" cy="41" r="40" fill="var(--green)"/>
      <circle cx="41" cy="41" r="35" fill="none" stroke="#fff" stroke-width="2"/>
      <rect x="33" y="24" width="20" height="16" fill="none" stroke="#fff" stroke-width="1.8"/>
      <polyline points="37,36 41,32 44,34 49,28" fill="none" stroke="#fff" stroke-width="1.5"/>
      <circle cx="30" cy="30" r="3" fill="#fff"/>
      <rect x="28" y="34" width="4" height="9" fill="#fff"/>
      <circle cx="31" cy="48" r="3" fill="#fff"/><path d="M26 57 Q26 52 31 52 Q36 52 36 57 Z" fill="#fff"/>
      <circle cx="41" cy="48" r="3" fill="#fff"/><path d="M36 57 Q36 52 41 52 Q46 52 46 57 Z" fill="#fff"/>
      <circle cx="51" cy="48" r="3" fill="#fff"/><path d="M46 57 Q46 52 51 52 Q56 52 56 57 Z" fill="#fff"/>
    </svg>
    <div class="service-title">WORKSHOPS</div>
    <p class="service-text">Knowledge work endeavors such as software development projects seem anything but clear when in process. One can demand</p>
    <div class="service-more">READMORE</div>
  </div>

  <h2 class="abs section-title" style="top:703px">OUR <span>BLOG</span></h2>
  <p class="abs section-intro" style="top:741px">Knowledge work endeavors such as software development projects seem anything but clear when in process. One can demand all the detailed status reports, stakeholder update meetings, and reassurances in the world</p>

  <article class="abs post" style="left:59px;top:786px">
    <div class="post-frame"><div class="post-image" role="img" aria-label="Photo of an engineer sketching a city skyline on a chalkboard" style="background:linear-gradient(135deg,#4f6b66,#7c9690 60%,#5c736e)"></div></div>
    <h3 class="post-title">SPEAKING AT SPRINTFEST 2016</h3>
    <p class="post-text">Nemo enim ipsam voluptatem quia voluptas sit asperna tur aut odit autuia consequuntur magni ratione</p>
    <div class="post-more">READ MORE &gt;&gt;</div>
  </article>

  <article class="abs post" style="left:258px;top:786px">
    <div class="post-frame"><div class="post-image" role="img" aria-label="Photo of an engineer in a hard hat reading plans against a city backdrop" style="background:linear-gradient(135deg,#d6e8f2,#9cc3d8 55%,#5f8fb0)"></div></div>
    <h3 class="post-title">SPEAKING AT SPRINTFEST 2016</h3>
    <p class="post-text">Nemo enim ipsam voluptatem quia voluptas sit asperna tur aut odit autuia consequuntur magni ratione</p>
    <div class="post-more">READ MORE &gt;&gt;</div>
  </article>

  <article class="abs post" style="left:456px;top:786px">
    <div class="post-frame"><div class="post-image" role="img" aria-label="Photo of two business people with briefcases in front of a concrete wall" style="background:linear-gradient(135deg,#c9c9c7,#a9a9a6 60%,#8d8d8a)"></div></div>
    <h3 class="post-title">SPEAKING AT SPRINTFEST 2016</h3>
    <p class="post-text">Nemo enim ipsam voluptatem quia voluptas sit asperna tur aut odit autuia consequuntur magni ratione</p>
    <div class="post-more">READ MORE &gt;&gt;</div>
  </article>

  <footer class="abs site-footer"></footer>
  <div class="abs footer-col" style="left:85px">
    <h4 class="footer-heading">COMPANY</h4>
    <ul><li>About us</li><li>Contact Us</li><li>My account</li><li>Orders history</li><li>Advanced search</li><li>Shipping</li></ul>
  </div>
  <div class="abs footer-col" style="left:204px">
    <h4 class="footer-heading">OUR RANGE</h4>
    <ul><li>Merchandise</li><li>Clothing</li><li>Caps &amp; Hats</li><li>Bags</li><li>Pens</li><li>Drinkware</li></ul>
  </div>
  <div class="abs footer-col" style="left:352px">
    <h4 class="footer-heading">SUPPORT</h4>
    <ul><li>FAQs</li><li>Privacy Policy</li><li>Recommendations</li><li>Contact</li></ul>
  </div>
  <div class="abs footer-col" style="left:461px">
    <h4 class="footer-heading">NEWSLETTER SIGN UP</h4>
    <p class="newsletter-note">Please sign up here for latest deals</p>
    <div class="newsletter-input">Email address</div>
    <div class="newsletter-button">SUBSCRIBE</div>
  </div>

  <div class="abs legal-bar"></div>
  <p class="abs legal-text">© 2016 drivpeak &nbsp;All right reserved &nbsp;Term of Use</p>
  <div class="abs social-links">
    <span class="social-chip" aria-label="Social profile"></span>
    <span class="social-chip" aria-label="Social profile"></span>
    <span class="social-chip" aria-label="Peerlinko profile"></span>
  </div>
</body>
</html>
```